Luxury Business Card Design for High-End Window Treatments

Gilded Slatworks
Custom Plantation Shutters & Architectural Shading Systems

⸻

BACK

Daniel Ferrowitz
Owner

Custom Interior & Exterior Window Treatments

919-555-0187
gildedslatworks.example

I have included a picture that I’m hoping we can use on the back, but I’m also wondering if you can get rid of the ladder? Should we get rid of shutters , shades and blinds underneath Gilded Slatworks?

Target Market(s)

High-end residential homeowners, custom home builders, architects, interior designers, and luxury renovation clients seeking premium plantation shutters and motorized architectural shading systems.

Industry/Entity Type

Custom Window treatments

Contact Information for Business Card

Front Gilded Slatworks Custom Plantation Shutters Motorized Architectural Shading Systems BACK Daniel Ferrowitz Owner 919-555-0187 GildedSlatworks.example Custom Interior & Exterior Window Treatments By Appointment

Requirements
Nice to have
• Not 100% sure on nice to halves or the color but you can definitely check out my website to get a better understanding of what I’m trying to do

```html
<!DOCTYPE html>
<html lang="en">
<head>
<meta charset="utf-8">
<title>Gilded Slatworks — Business Card</title>
<link rel="stylesheet" href="https://fonts.googleapis.com/css2?family=Cormorant+Garamond:wght@400;600;700&family=Poppins:wght@300;400&display=swap">
<style>
  :root {
    --backdrop: #1c1c1c;
    --card-black: #0b0b0b;
    --card-black-soft: #151515;
    --gold: #c9b25c;
    --gold-bright: #ddc66a;
    --white: #f4f4f4;
    --sky: #6f9fd6;
    --navy: #1d2638;
    --shade: #0d1119;
  }
  * { box-sizing: border-box; margin: 0; padding: 0; }
  html, body {
    width: 1200px; height: 900px; overflow: hidden;
    background: var(--backdrop);
  }
  .sheet {
    width: 1200px; height: 900px;
    display: flex; flex-direction: column; align-items: center; justify-content: center;
    gap: 40px;
  }
  .card {
    position: relative;
    width: 700px; height: 400px;
    border-radius: 22px;
    overflow: hidden;
    border-bottom: 6px solid var(--gold);
  }

  /* Contact side */
  .card--contact {
    background: radial-gradient(ellipse at 70% 20%, var(--card-black-soft), var(--card-black) 70%);
  }
  .brand-name {
    position: absolute; left: 70px; top: 120px;
    width: 250px;
    font-family: "Cormorant Garamond", serif;
    font-weight: 400;
    font-size: 58px; line-height: 1.0;
    color: var(--gold);
  }
  .divider {
    position: absolute; left: 340px; top: 110px;
    width: 1px; height: 150px;
    background: var(--gold);
    opacity: 0.7;
  }
  .contact {
    position: absolute; left: 375px; top: 112px;
  }
  .contact__name {
    font-family: "Cormorant Garamond", serif;
    font-weight: 700; font-size: 34px; line-height: 1;
    color: var(--gold-bright);
  }
  .contact__role {
    font-family: "Poppins", sans-serif;
    font-weight: 300; font-size: 18px; line-height: 1.2;
    color: var(--white);
  }
  .contact__list { list-style: none; margin-top: 28px; }
  .contact__item {
    display: flex; align-items: center; gap: 12px;
    font-family: "Poppins", sans-serif;
    font-weight: 300; font-size: 18px; line-height: 1.6;
    color: var(--white);
  }
  .contact__item svg { width: 18px; height: 18px; flex: none; }
  .tagline {
    position: absolute; left: 0; right: 0; bottom: 34px;
    text-align: center;
    font-family: "Cormorant Garamond", serif;
    font-weight: 600; font-size: 21px; letter-spacing: 0.5px;
    color: var(--gold);
  }

  /* Photo side */
  .card--photo { background: var(--shade); }
  .photo {
    position: absolute; inset: 0;
    background: linear-gradient(160deg, var(--sky) 0%, #c8c3b4 22%, var(--navy) 45%, var(--shade) 80%);
  }
  .services {
    position: absolute; right: 60px; bottom: 50px;
    font-family: "Cormorant Garamond", serif;
    font-weight: 600; font-size: 22px; line-height: 1.3;
    color: var(--gold);
  }
</style>
</head>
<body>
<main class="sheet">
  <section class="card card--contact">
    <h1 class="brand-name">Gilded Slatworks</h1>
    <div class="divider"></div>
    <div class="contact">
      <p class="contact__name">Daniel Ferrowitz</p>
      <p class="contact__role">Owner</p>
      <ul class="contact__list">
        <li class="contact__item">
          <svg viewBox="0 0 24 24" fill="none" stroke="#c9b25c" stroke-width="2"><path d="M5 3h4l2 5-2.5 1.5a11 11 0 0 0 6 6L16 13l5 2v4a2 2 0 0 1-2 2A16 16 0 0 1 3 5a2 2 0 0 1 2-2z"/></svg>
          919-555-0187
        </li>
        <li class="contact__item">
          <svg viewBox="0 0 24 24" fill="none" stroke="#c9b25c" stroke-width="2"><rect x="3" y="5" width="18" height="14" rx="1"/><path d="M3 6l9 7 9-7"/></svg>
          GildedSlatworks.example
        </li>
      </ul>
    </div>
    <p class="tagline">Custom Interior &amp; Exterior Window Treatments By Appointment</p>
  </section>

  <section class="card card--photo">
    <div class="photo" role="img" aria-label="Photograph of a covered home patio with motorized exterior shades lowered between white columns under a blue sky"></div>
    <p class="services">Gilded Slatworks Custom<br>Plantation Shutters Motorized<br>Architectural Shading Systems</p>
  </section>
</main>
</body>
</html>
```